依頼詳細
【外貨両替】
外貨両替は学校へ出向いて行う、出張両替とご自宅へ外貨をお届けする外貨宅配の2プランがございます。どちらのプランにするかは学校の意向や参加者の規模や要望によります。

【フェリシオンクレスト】
外貨両替(現金)以外のお金としてトラベルマネーカード(フェリシオンクレスト)の紹介をしております。こちらはキャッシュレスに対応したカードで使い方はクレジットカードと同じですが、チャージした金額の範囲でご利用頂けるカードです。

今回、制作するパンフレットは旅行会社から旅行参加者へ配布してご質問等があれば旅行会社ではなく直接当社が窓口となり、旅行参加者からの質問等を受付いたします。
今回制作するパンフレットとは別に両替の申込書面、フェリシオンクレストの申込書面は別となります。あくまでも全体の案内、問い合わせ先の案内をするパンフレットです。
記載項目
資料を添付致しますので、要点をまとめてA4サイズカラー裏表で制作をお願い致します。
サイズ
A4
ページ数
両面
希望イメージ
シンプル 複雑
単色 カラフル
暗い 明るい
日常 高級
遊び心 厳粛
未来的 伝統的
女性的 男性的
希望する色
赤系、青系
納品ファイル
• イラストレーター形式 (.ai)
補足説明
■ 選んだ理由

社内で選考した結果、一番わかりやすく好評であった為当選とさせていただきました。

■ 提案者全員のお礼・コメント

この度は短期間でしたが、沢山の方にご参加頂き、またどの提案も良いものばかりでした。
また次回依頼する場合も宜しくお願い致します。

```html
<!DOCTYPE html>
<html lang="ja">
<head>
<meta charset="utf-8">
<title>外貨両替のお役立ちガイド</title>
<link href="https://fonts.googleapis.com/css2?family=Noto+Sans+JP:wght@400;500;700;900&display=swap" rel="stylesheet">
<style>
:root{
  --navy:#12306b;
  --blue:#1d5fbf;
  --sky:#e6f0fb;
  --red:#d9282f;
  --yellow:#ffd23c;
  --ink:#1f2a44;
  --line:#c9d6ea;
  --white:#ffffff;
}
*{margin:0;padding:0;box-sizing:border-box}
html,body{width:849px;height:1200px;overflow:hidden;background:var(--white)}
body{font-family:"Noto Sans JP",sans-serif;color:var(--ink)}
.page{position:relative;width:849px;height:1200px;overflow:hidden;background:var(--white)}

.brand{position:absolute;left:34px;top:18px;display:flex;align-items:center;gap:8px;color:var(--blue);font-weight:700;font-size:18px}
.brand-dot{width:20px;height:20px;border-radius:50%;background:var(--blue)}
.audience-tag{position:absolute;right:34px;top:20px;border:1px solid var(--navy);color:var(--navy);font-size:10px;padding:3px 10px}

.hero{position:absolute;left:0;top:58px;width:849px;height:390px}
.hero svg{position:absolute;inset:0}
.hero-kicker{position:absolute;top:28px;width:100%;text-align:center;color:var(--white);font-weight:700;font-size:22px;letter-spacing:2px}
.hero-kicker span{color:#8fb8ff;margin:0 10px}
.hero-title{position:absolute;top:78px;width:100%;text-align:center;line-height:1.1}
.hero-title .main{display:block;font-size:62px;font-weight:900;color:var(--blue);letter-spacing:3px}
.hero-title .main small{font-size:44px;color:var(--navy)}
.hero-title .sub{display:block;font-size:50px;font-weight:900;color:var(--navy);letter-spacing:2px;margin-top:6px}
.coin{position:absolute;width:86px;height:86px;border-radius:50%;background:var(--white);border:5px solid var(--blue);color:var(--blue);font-weight:900;font-size:46px;display:flex;align-items:center;justify-content:center}
.coin.yen{left:120px;top:100px}
.coin.dollar{right:120px;top:100px}
.seal{position:absolute;right:112px;top:190px;width:70px;height:70px;border-radius:50%;background:var(--red);color:var(--white);font-weight:700;text-align:center;font-size:12px;line-height:1.05;padding-top:12px}
.seal b{font-size:24px}
.hero-lead{position:absolute;top:286px;width:100%;text-align:center;color:var(--white);font-size:13.5px;line-height:1.7}

.section{position:absolute;left:34px;width:781px;border:2px solid var(--line);border-radius:10px;background:var(--white)}
.section-head{display:flex;align-items:center;gap:10px;background:var(--red);color:var(--white);font-weight:700;font-size:20px;padding:8px 22px;border-radius:8px 8px 0 0}
.section-head svg{flex:none}
.exchange{top:458px;height:372px}
.plans{display:flex;gap:22px;padding:16px 22px}
.plan{flex:1;border:2px solid var(--blue);border-radius:10px;overflow:hidden}
.plan-tag{background:var(--blue);color:var(--white);text-align:center;font-weight:700;font-size:14px;padding:6px}
.plan-name{display:flex;align-items:center;gap:10px;padding:12px 16px 8px;font-size:24px;font-weight:900;color:var(--navy)}
.plan-name .badge{font-size:10px;font-weight:700;color:var(--white);background:var(--red);padding:2px 6px;border-radius:3px;margin-left:auto}
.plan-icon{width:40px;height:40px;border-radius:8px;background:var(--sky)}
.ticks{list-style:none;padding:4px 16px 14px}
.ticks li{display:flex;align-items:flex-start;gap:8px;font-size:14px;font-weight:500;line-height:1.45;padding:5px 0;border-bottom:1px dashed var(--line)}
.ticks li:last-child{border-bottom:none}
.ticks svg{flex:none;margin-top:3px}
.ticks em{font-style:normal;color:var(--red);font-weight:700}

.card-info{top:846px;height:286px}
.card-body{display:flex;gap:20px;padding:16px 22px}
.card-left{width:372px;display:flex;gap:14px}
.card-visual{flex:none;width:150px;height:96px;border-radius:8px;background:linear-gradient(135deg,#2a3b63,#6b7ea8)}
.card-text{font-size:13px;line-height:1.75}
.card-text b{color:var(--blue)}
.card-points{flex:1;list-style:none}
.card-points li{display:flex;align-items:center;gap:8px;background:var(--sky);border-radius:16px;font-size:13.5px;font-weight:700;color:var(--navy);padding:7px 12px;margin-bottom:8px}

.more{position:absolute;right:34px;bottom:26px;display:flex;align-items:center;gap:10px;background:var(--navy);color:var(--white);font-weight:700;font-size:15px;padding:9px 22px;border-radius:22px}
</style>
</head>
<body>
<div class="page">
  <div class="brand"><span class="brand-dot"></span>Voyage Assist</div>
  <div class="audience-tag">教育機関向け外貨案内</div>

  <header class="hero">
    <svg width="849" height="390" viewBox="0 0 849 390">
      <rect width="849" height="390" fill="#12306b"/>
      <path d="M0 62 H849 V236 Q424 290 0 236 Z" fill="#ffffff"/>
      <path d="M0 236 Q424 290 849 236 V246 Q424 302 0 246 Z" fill="#d9282f"/>
    </svg>
    <p class="hero-kicker"><span>＼</span>学校・教育旅行で必要な<span>／</span></p>
    <h1 class="hero-title">
      <span class="main">外貨両替<small>の</small></span>
      <span class="sub">お役立ちガイド</span>
    </h1>
    <div class="coin yen">¥</div>
    <div class="coin dollar">$</div>
    <div class="seal">最大<br><b>32</b>通貨</div>
    <p class="hero-lead">アフターコロナの現在、ほとんどの銀行は外貨両替の取り扱いを中止しました。<br>空港でも外貨両替店舗の縮小等で、両替を取り扱う環境はよくありません。<br>ご出発前の事前準備として、外貨の両替を済ませて<br>スムーズに飛び立ちませんか？</p>
  </header>

  <section class="section exchange">
    <h2 class="section-head">
      <svg width="22" height="22" viewBox="0 0 22 22"><circle cx="11" cy="11" r="10" fill="#fff"/><text x="11" y="16" text-anchor="middle" font-size="14" font-weight="700" fill="#d9282f">¥</text></svg>
      外貨両替について
    </h2>
    <div class="plans">
      <article class="plan">
        <div class="plan-tag">学校へ出向いて行う</div>
        <h3 class="plan-name"><span class="plan-icon" role="img" aria-label="出張両替のイラスト"></span>出張外貨両替<span class="badge">手数料無料</span></h3>
        <ul class="ticks">
          <li><svg width="14" height="14" viewBox="0 0 14 14"><path d="M2 7l3 3 7-7" stroke="#d9282f" stroke-width="2.4" fill="none"/></svg><span><em>32通貨</em>の両替が可能</span></li>
          <li><svg width="14" height="14" viewBox="0 0 14 14"><path d="M2 7l3 3 7-7" stroke="#d9282f" stroke-width="2.4" fill="none"/></svg><span>両替レートは金融機関よりも<em>お得なレート！</em></span></li>
          <li><svg width="14" height="14" viewBox="0 0 14 14"><path d="M2 7l3 3 7-7" stroke="#d9282f" stroke-width="2.4" fill="none"/></svg><span>学生が使い易い少額紙幣が中心</span></li>
          <li><svg width="14" height="14" viewBox="0 0 14 14"><path d="M2 7l3 3 7-7" stroke="#d9282f" stroke-width="2.4" fill="none"/></svg><span>紙幣は可能な限り新札紙幣をご用意</span></li>
          <li><svg width="14" height="14" viewBox="0 0 14 14"><path d="M2 7l3 3 7-7" stroke="#d9282f" stroke-width="2.4" fill="none"/></svg><span>両替計算書は各学生ごとにご案内</span></li>
        </ul>
      </article>
      <article class="plan">
        <div class="plan-tag">ご自宅へ外貨をお届けする</div>
        <h3 class="plan-name"><span class="plan-icon" role="img" aria-label="外貨宅配のイラスト"></span>外貨宅配<span class="badge">送料無料</span></h3>
        <ul class="ticks">
          <li><svg width="14" height="14" viewBox="0 0 14 14"><path d="M2 7l3 3 7-7" stroke="#d9282f" stroke-width="2.4" fill="none"/></svg><span><em>17通貨</em>への両替が可能</span></li>
          <li><svg width="14" height="14" viewBox="0 0 14 14"><path d="M2 7l3 3 7-7" stroke="#d9282f" stroke-width="2.4" fill="none"/></svg><span><em>24時間ネット受付！</em></span></li>
          <li><svg width="14" height="14" viewBox="0 0 14 14"><path d="M2 7l3 3 7-7" stroke="#d9282f" stroke-width="2.4" fill="none"/></svg><span>学生が使い易い少額紙幣が中心</span></li>
          <li><svg width="14" height="14" viewBox="0 0 14 14"><path d="M2 7l3 3 7-7" stroke="#d9282f" stroke-width="2.4" fill="none"/></svg><span>送料は全国無料にお届け</span></li>
          <li><svg width="14" height="14" viewBox="0 0 14 14"><path d="M2 7l3 3 7-7" stroke="#d9282f" stroke-width="2.4" fill="none"/></svg><span>紙幣は可能な限り新札紙幣をご用意</span></li>
        </ul>
      </article>
    </div>
  </section>

  <section class="section card-info">
    <h2 class="section-head">
      <svg width="24" height="18" viewBox="0 0 24 18"><rect x="1" y="1" width="22" height="16" rx="2" fill="#fff"/><rect x="1" y="5" width="22" height="3" fill="#d9282f"/></svg>
      フェリシオンクレストについて
    </h2>
    <div class="card-body">
      <div class="card-left">
        <div class="card-visual" role="img" aria-label="トラベルマネーカードの券面写真"></div>
        <p class="card-text">外貨両替（現金）以外のお金としてトラベルマネーカード（<b>フェリシオンクレスト</b>）の紹介をしております。こちらはキャッシュレスに対応したカードで使い方はクレジットカードと同じですが、チャージした金額の範囲でご利用頂けるカードです。</p>
      </div>
      <ul class="card-points">
        <li><svg width="14" height="14" viewBox="0 0 14 14"><path d="M2 7l3 3 7-7" stroke="#d9282f" stroke-width="2.4" fill="none"/></svg>審査がなく中学生から発行できます</li>
        <li><svg width="14" height="14" viewBox="0 0 14 14"><path d="M2 7l3 3 7-7" stroke="#d9282f" stroke-width="2.4" fill="none"/></svg>使いすぎる心配がないプリペイド型</li>
        <li><svg width="14" height="14" viewBox="0 0 14 14"><path d="M2 7l3 3 7-7" stroke="#d9282f" stroke-width="2.4" fill="none"/></svg>現金引き出しもショッピングもこれ1枚で</li>
        <li><svg width="14" height="14" viewBox="0 0 14 14"><path d="M2 7l3 3 7-7" stroke="#d9282f" stroke-width="2.4" fill="none"/></svg>スペアカードをもれなく付帯、紛失時も安心</li>
        <li><svg width="14" height="14" viewBox="0 0 14 14"><path d="M2 7l3 3 7-7" stroke="#d9282f" stroke-width="2.4" fill="none"/></svg>残高管理は日本円の他に通貨に対応</li>
      </ul>
    </div>
  </section>

  <div class="more">詳しくは裏面をご確認ください
    <svg width="18" height="18" viewBox="0 0 18 18"><circle cx="9" cy="9" r="8" fill="#fff"/><path d="M7 5l4 4-4 4" stroke="#12306b" stroke-width="2" fill="none"/></svg>
  </div>
</div>
</body>
</html>
```